Flyer for a Payroll and Bookkeeping Companmy

Need a brochure to highlight our costs and service to hand out to clients.

Please see attachments for more information.

It Service

```html
<!DOCTYPE html>
<html lang="en">
<head>
<meta charset="utf-8">
<title>Harbor Ridge – Bookkeeping &amp; Payroll Pricing</title>
<link href="https://fonts.googleapis.com/css2?family=Anton&family=PT+Sans:wght@400;700&family=Roboto:wght@400;700&display=swap" rel="stylesheet">
<style>
:root{
  --orange:#f26a10;
  --orange-dark:#7a2a06;
  --blue:#1e6ff2;
  --ink:#111;
  --band:#1e2022;
  --rule:#3a3a3a;
  --row-alt:#f2f3f3;
  --white:#fff;
}
*{box-sizing:border-box;margin:0;padding:0}
html,body{width:934px;height:1200px;overflow:hidden;background:var(--white)}
.flyer{position:relative;width:934px;height:1200px;font-family:"Roboto",Arial,sans-serif;color:var(--ink);overflow:hidden}

/* header */
.brand{position:absolute;left:22px;top:78px;display:flex;align-items:center;gap:8px}
.brand-dot{width:20px;height:20px;border-radius:50%;background:var(--blue)}
.brand-name{font-family:"PT Sans",sans-serif;font-weight:700;color:var(--blue);font-size:21px;line-height:1.05}
.brand-name small{display:block;font-size:12px;font-weight:400;color:var(--orange)}
.title{position:absolute;left:290px;top:30px;font-family:"Anton",sans-serif;font-size:70px;line-height:1;color:var(--orange);letter-spacing:.5px}

/* pricing band */
.band-photo{position:absolute;left:0;top:122px;width:934px;height:478px;
  background:linear-gradient(90deg,#f5c98a 0%,#f7ddc9 10%,#eeeae4 14%,#e4e9ea 88%,#a8b2a0 92%,#cfd3d3 100%)}
.pricing{position:absolute;left:111px;top:133px;width:709px;border-collapse:collapse;table-layout:fixed;font-size:15px}
.pricing col.svc{width:268px}
.pricing col.tier{width:151px}
.pricing col.tier-last{width:139px}
.pricing th,.pricing td{border:1px solid var(--rule);text-align:center;vertical-align:middle}
.pricing .head th{background:var(--orange-dark);color:#fff;font-weight:400;height:20px;font-size:14px;line-height:1}
.pricing .head th.svc-label{background:#000;letter-spacing:2px;font-size:16px}
.pricing .price td{height:37px;background:var(--orange);color:#fff;font-size:26px}
.pricing .price td.blank{background:#fff}
.pricing tbody tr{height:51px;background:#fff}
.pricing tbody tr:nth-child(even){background:var(--row-alt)}
.pricing .svc-name{text-align:right;padding-right:9px;font-weight:700;font-size:15.5px}
.pricing .svc-name small{display:block;font-weight:400;font-size:11.5px;margin-top:2px}
.pricing .qty small{display:block;font-size:11.5px}
.pricing .qty{font-size:17px;line-height:1.05}
.pricing .freq{display:block;color:var(--orange);font-size:14.5px;margin-top:2px}
.tick{width:20px;height:20px;display:block;margin:0 auto}

/* statement band */
.statement{position:absolute;left:0;top:600px;width:934px;height:131px;background:var(--band);color:#fff;font-family:"PT Sans",sans-serif;padding:4px 0 0 53px}
.statement h2{font-size:29px;font-weight:400;line-height:1.1}
.statement h3{font-size:29px;font-weight:400;line-height:1.1}
.statement h3 .a{color:var(--blue)} .statement h3 .b{color:var(--orange)}
.statement p{font-size:19.5px;line-height:1.05;margin-top:3px;max-width:835px}

/* payroll */
.payroll-photo{position:absolute;left:0;top:731px;width:520px;height:469px;
  background:linear-gradient(90deg,#9fa6ad 0%,#c3c8cd 40%,rgba(255,255,255,0) 100%)}
.tag{position:absolute;left:52px;background:var(--blue);color:#fff;font-family:"PT Sans",sans-serif;font-weight:700;font-size:46px;line-height:1;padding:4px 10px 3px}
.tag.one{top:746px}
.tag.two{top:804px}
.rate{position:absolute;left:430px;top:754px;width:424px;text-align:center;font-size:45px;line-height:1.04}
.rate .free{color:var(--orange)}
.notes{position:absolute;left:80px;top:970px;width:800px;font-size:17px;line-height:1.6;text-align:center}
.notes .accent{color:var(--orange)}
.contact-title{position:absolute;left:53px;top:1046px;font-family:"PT Sans",sans-serif;font-weight:700;font-size:22px}
.contact-rule{position:absolute;left:0;top:1079px;width:934px;height:1px;background:var(--orange)}
.contact{position:absolute;display:flex;align-items:center;gap:10px;font-family:"PT Sans",sans-serif;font-size:12.5px;line-height:1.6}
.contact .ic{width:32px;height:32px;border-radius:50%;background:var(--orange);display:flex;align-items:center;justify-content:center;flex:none}
.contact.phone{left:54px;top:1106px}
.contact.mail{left:297px;top:1105px}
.contact.addr{left:576px;top:1096px}
</style>
</head>
<body>
<svg width="0" height="0" style="position:absolute">
  <symbol id="tick" viewBox="0 0 20 20"><path d="M1 11 L7 17 L19 3 L16.5 1.5 L7 12.5 L3.5 8.5 Z" fill="#f26a10"/></symbol>
</svg>
<div class="flyer">
  <header>
    <div class="brand"><span class="brand-dot"></span><div class="brand-name">Harbor Ridge<small>Payroll and Bookkeeping</small></div></div>
    <h1 class="title">Bookkeeping Pricing</h1>
  </header>

  <div class="band-photo" role="img" aria-label="Tax forms on a desk beside a calculator and green plant"></div>

  <table class="pricing">
    <colgroup><col class="svc"><col class="tier"><col class="tier"><col class="tier-last"></colgroup>
    <thead>
      <tr class="head"><th class="svc-label">SERVICES</th><th>Premium</th><th>Entrepreneur</th><th>Growth</th></tr>
      <tr class="price"><td class="blank"></td><td>$999</td><td>$599</td><td>$299</td></tr>
    </thead>
    <tbody>
      <tr><td class="svc-name">Employees</td><td class="qty"><small>Around</small>10+</td><td class="qty"><small>Around</small>5-9</td><td class="qty"><small>Around</small>2-5</td></tr>
      <tr><td class="svc-name">Transactions / Month</td><td class="qty"><small>Up to</small>250</td><td class="qty"><small>Up to</small>150</td><td class="qty"><small>Up to</small>75</td></tr>
      <tr><td class="svc-name">Bookkeeping</td>
        <td><svg class="tick"><use href="#tick"/></svg><span class="freq">Weekly</span></td>
        <td><svg class="tick"><use href="#tick"/></svg><span class="freq">Weekly</span></td>
        <td><svg class="tick"><use href="#tick"/></svg><span class="freq">Monthly</span></td></tr>
      <tr><td class="svc-name">Financial Reports &amp; Review</td>
        <td><svg class="tick"><use href="#tick"/></svg><span class="freq">Monthly</span></td>
        <td><svg class="tick"><use href="#tick"/></svg><span class="freq">Monthly</span></td>
        <td><svg class="tick"><use href="#tick"/></svg><span class="freq">Monthly</span></td></tr>
      <tr><td class="svc-name">Support<small>(Phone and Chat)</small></td>
        <td><svg class="tick"><use href="#tick"/></svg></td><td><svg class="tick"><use href="#tick"/></svg></td><td><svg class="tick"><use href="#tick"/></svg></td></tr>
      <tr><td class="svc-name">Online Collaboration Portal<small>(Shared Folders)</small></td>
        <td><svg class="tick"><use href="#tick"/></svg></td><td><svg class="tick"><use href="#tick"/></svg></td><td><svg class="tick"><use href="#tick"/></svg></td></tr>
      <tr><td class="svc-name">Business Tax Return</td>
        <td><svg class="tick"><use href="#tick"/></svg></td><td><svg class="tick"><use href="#tick"/></svg></td><td class="qty">$799</td></tr>
      <tr><td class="svc-name">Bill Pay<small>(with Approval Process)</small></td>
        <td><svg class="tick"><use href="#tick"/></svg><span class="freq">$5 / Payment</span></td><td class="qty">X</td><td class="qty">X</td></tr>
    </tbody>
  </table>

  <section class="statement">
    <h2>Harbor Ridge</h2>
    <h3><span class="a">Payroll &amp;</span> <span class="b">Bookkeeping</span></h3>
    <p>We are dedicated to freeing your mind and your time from the day to day demands of accounting while you focus on growing your business.</p>
  </section>

  <div class="payroll-photo" role="img" aria-label="Two colleagues working at a whiteboard in a bright office"></div>
  <div class="tag one">Simplified</div>
  <div class="tag two">Payroll Pricing</div>
  <div class="rate">$25 per Payroll<br>+$5 per Employee<br><span class="free">No Set Up Fees!</span></div>
  <p class="notes">Direct deposit only, add $20 per payroll if you elect to have paper checks shipped to you.<br>Minimum charge of two payrolls per month. &nbsp;<span class="accent">Cost per employee drops to $4 after 20 employees.</span></p>

  <h4 class="contact-title">Get in Touch</h4>
  <div class="contact-rule"></div>
  <div class="contact phone"><span class="ic"><svg width="16" height="16" viewBox="0 0 24 24"><path fill="#111" d="M6.6 10.8a15 15 0 0 0 6.6 6.6l2.2-2.2a1 1 0 0 1 1-.25 11.4 11.4 0 0 0 3.6.57 1 1 0 0 1 1 1V20a1 1 0 0 1-1 1A17 17 0 0 1 3 4a1 1 0 0 1 1-1h3.5a1 1 0 0 1 1 1c0 1.25.2 2.45.57 3.57a1 1 0 0 1-.25 1z"/></svg></span>555-014-7730</div>
  <div class="contact mail"><span class="ic"><svg width="16" height="16" viewBox="0 0 24 24"><circle cx="12" cy="12" r="9" fill="none" stroke="#111" stroke-width="2.5"/><path d="M3 12h18M12 3c3 3 3 15 0 18M12 3c-3 3-3 15 0 18" fill="none" stroke="#111" stroke-width="1.5"/></svg></span>hello@harborridge.example</div>
  <div class="contact addr"><span class="ic"><svg width="14" height="16" viewBox="0 0 24 28"><path fill="#111" d="M12 0a10 10 0 0 0-10 10c0 7.5 10 18 10 18s10-10.5 10-18A10 10 0 0 0 12 0zm0 14a4 4 0 1 1 0-8 4 4 0 0 1 0 8z"/></svg></span><span>418 Tidewater Avenue, Suite B Juneau,<br>Alaska 99801</span></div>
</div>
</body>
</html>
```